Fenwick Nutrition Therapy needs a business card design

I need a business card design for my private practice. Green is my favorite color. I would like the back of the card to include an area for future appointment dates and time. I provide nutrition therapy to individuals, groups and families. I work a lot with adolescents and women who have eating disorders, but also work with athletes.
Updates

Reason: I received several new designs and would like to take some time reviewing them.

Target Market(s)

I am working primarily with women, but also men (mostly athletes). I work with a lot of runners. I work with people who are 14-60's.

Industry/Entity Type

Nutrition

Font styles to use
Serif
Sans Serif

Colors
9bcb3c
acd037

Requirements
Nice to have
• I would love to have 'Fenwick' incorporated into the design since it is my last name. If possible, I'd love to have an actual moon if it looks professional.

A picture of food could also be on the card if it is simple, but not sure how it would look with Fenwick. I am open to ideas for both Fenwick and a picture of a food item.

Other font style are fine as long as they are easy to read.

```html
<!DOCTYPE html>
<html lang="en">
<head>
<meta charset="utf-8">
<title>Fenwick Nutrition Therapy – Business Card</title>
<link href="https://fonts.googleapis.com/css2?family=Gelasio:wght@400;500&display=swap" rel="stylesheet">
<style>
  :root {
    --backdrop: #0b1e2c;
    --card-light: #a6f22a;
    --card-mid: #8fe60c;
    --card-deep: #79cc06;
    --ink: #4d8a12;
    --ink-soft: rgba(77, 138, 18, 0.45);
    --moon-light: #f4fbe4;
    --moon-shade: #d6ecb2;
  }
  html, body {
    margin: 0;
    width: 1200px;
    height: 1000px;
    overflow: hidden;
    background: var(--backdrop);
    font-family: "Gelasio", Georgia, serif;
  }
  .canvas { position: relative; width: 1200px; height: 1000px; }
  .card {
    position: absolute;
    border-radius: 22px;
    overflow: hidden;
    background: linear-gradient(160deg, var(--card-light) 0%, var(--card-mid) 50%, var(--card-deep) 100%);
    color: var(--ink);
  }
  .card--front { left: 38px; top: 22px; width: 822px; height: 460px; }
  .card--back  { left: 340px; top: 510px; width: 828px; height: 465px; }
  .moon {
    position: absolute;
    border-radius: 50%;
    background: radial-gradient(circle at 45% 40%, var(--moon-light) 0%, var(--moon-shade) 100%);
  }
  .card--front .moon { left: 20px; top: 18px; width: 210px; height: 210px; opacity: 0.9; }
  .card--back .moon  { left: 23px; top: 127px; width: 210px; height: 210px; opacity: 0.55; }
  .text { position: absolute; margin: 0; white-space: nowrap; line-height: 1; }
  .brand { right: 14px; top: 88px; font-size: 56px; }
  .person { right: 16px; top: 230px; text-align: right; }
  .person__name { display: block; font-size: 50px; }
  .person__credentials { display: block; font-size: 30px; margin-top: -4px; }
  .contact { right: 16px; top: 344px; text-align: right; font-size: 21px; line-height: 26.5px; }
  .appointment__title { left: 0; right: 0; top: 16px; text-align: center; font-size: 56px; }
  .appointment__labels { left: 0; right: 0; top: 92px; text-align: center; font-size: 48px; word-spacing: 0.3em; }
  .brand--faint { left: 40px; top: 196px; font-size: 60px; color: var(--ink-soft); }
  .slots { position: absolute; left: 0; top: 0; }
</style>
</head>
<body>
<main class="canvas">
  <section class="card card--front" aria-label="Card front">
    <div class="moon" role="img" aria-label="Full moon illustration"></div>
    <h1 class="text brand" style="font-weight:400">Fenwick Nutrition Therapy</h1>
    <p class="text person">
      <span class="person__name">Dana Harlow Fenwick</span>
      <span class="person__credentials">MS, RD, LDN</span>
    </p>
    <p class="text contact">
      Fax: 555.201.4470<br>
      Phone: 555.201.4471<br>
      Email: dhfenwick@example.net<br>
      Address: 4810 Linden Hollow Road, Maple Falls, TN 37000
    </p>
  </section>

  <section class="card card--back" aria-label="Card back">
    <div class="moon" role="img" aria-label="Faint full moon illustration"></div>
    <p class="text brand--faint">Fenwick Nutrition Therapy</p>
    <h2 class="text appointment__title" style="font-weight:400">Your appointment:</h2>
    <p class="text appointment__labels">Date | Time</p>
    <svg class="slots" width="828" height="465" viewBox="0 0 828 465" aria-hidden="true">
      <g stroke="#4d8a12" stroke-width="2.5">
        <line x1="90" y1="195" x2="368" y2="195"/><line x1="465" y1="195" x2="742" y2="195"/>
        <line x1="90" y1="245" x2="368" y2="245"/><line x1="465" y1="245" x2="742" y2="245"/>
        <line x1="90" y1="295" x2="368" y2="295"/><line x1="465" y1="295" x2="742" y2="295"/>
        <line x1="90" y1="345" x2="368" y2="345"/><line x1="465" y1="345" x2="742" y2="345"/>
        <line x1="90" y1="395" x2="368" y2="395"/><line x1="465" y1="395" x2="742" y2="395"/>
        <line x1="90" y1="445" x2="368" y2="445"/><line x1="465" y1="445" x2="742" y2="445"/>
      </g>
    </svg>
  </section>
</main>
</body>
</html>
```